Salon Vireau

menu design, menu change,
will send hand written rough draft soon

Reason: Got off to a slow start. Things are progressing now. Thank you.

Target Market(s)

18-60 yr olds, blue collar & professionals, middle class, median income, families,upscale - casual- steakhouse concept

Industry/Entity Type

Restaurant

Colors
f68d4c
f37122
f78f20
faa54b
ffc214
fece3e
fbee3e
fbed22
333333

Requirements
Must have
• Front cover, back cover. 2 inside views
Nice to have
• 8 x 14 page size

```html
<!DOCTYPE html>
<html lang="en">
<head>
<meta charset="utf-8">
<title>Salon Vireau — Menu</title>
<link href="https://fonts.googleapis.com/css2?family=Montserrat:wght@400;500;700&family=Titillium+Web:wght@300;400;700&display=swap" rel="stylesheet">
<style>
:root{
  --backdrop:#e4e1dc;
  --paper:#ffffff;
  --yellow:#f5ee3e;
  --gold:#ffc214;
  --orange:#f37122;
  --ink:#333333;
  --line:#222222;
  --muted:#6a6a6a;
}
*{margin:0;padding:0;box-sizing:border-box}
html,body{width:1200px;height:1200px;overflow:hidden;background:var(--backdrop)}
body{font-family:"Montserrat",sans-serif;color:var(--ink)}
.stage{position:absolute;left:0;top:0;width:1500px;height:1500px;transform:scale(.8);transform-origin:0 0}
.sheet{position:absolute;background:var(--paper);box-shadow:0 6px 18px rgba(0,0,0,.25)}
.sheet--front{left:271px;top:28px;width:788px;height:688px}
.sheet--inside{left:449px;top:773px;width:788px;height:689px;overflow:hidden}
.abs{position:absolute}
.panel-yellow{position:absolute;background:var(--yellow)}
.frame{position:absolute;border:2px solid var(--line)}
.heading{font-family:"Titillium Web",sans-serif;line-height:1}
.heading .kicker{display:block;font-weight:300;font-size:13px;letter-spacing:.5px}
.heading .main{display:block;font-weight:700;font-size:19px;letter-spacing:.3px}
.heading .note{display:block;font-family:"Montserrat",sans-serif;font-size:6.5px;color:var(--muted);margin-top:2px}
.heading .note b{color:var(--ink);font-weight:500}
.dish{position:absolute;font-size:7.6px;line-height:1.3}
.dish h4{font-size:8.2px;font-weight:700;line-height:1.3}
.dish p{font-weight:400}
.dish .price{font-size:12px;font-weight:700;display:block;margin-bottom:3px}
.price-tag{position:absolute;font-size:12px;font-weight:700}
.price-sm{position:absolute;font-size:8.5px;font-weight:700}
.brand{position:absolute;left:500px;top:36px;width:180px;text-align:center;font-family:"Titillium Web",sans-serif}
.brand .intro{font-size:7px;color:var(--muted)}
.brand .name{font-size:24px;font-weight:700;color:var(--orange);line-height:1;letter-spacing:.5px}
.brand .served{font-family:"Montserrat",sans-serif;font-size:7px;color:var(--muted);margin-top:2px}
.brand .served b{display:block;font-size:8.5px;color:var(--ink)}
.label{position:absolute;font-family:"Titillium Web",sans-serif;font-weight:700;text-align:center;color:var(--ink)}
.label--gold{background:var(--gold)}
.label--premium{left:501px;top:417px;width:180px;height:38px;font-size:16px;line-height:1}
.label--premium .main{display:block;padding-top:6px}
.label--premium .sub{display:block;font-weight:400;font-size:11px;letter-spacing:1.5px}
.label--premium .dot{position:absolute;top:16px;width:5px;height:5px;border-radius:50%;background:var(--ink)}
.center-note{position:absolute;text-align:center;font-size:6.5px;color:var(--muted);line-height:1.5}
.center-note b{color:var(--ink);font-weight:500}
.cut{font-size:6.5px;color:var(--muted);margin-right:14px}
.advisory{position:absolute;font-size:4.8px;color:var(--muted)}
.advisory b{color:var(--ink);font-weight:700;font-variant:small-caps}
.section-title{position:absolute;font-family:"Titillium Web",sans-serif;font-weight:700;font-size:19px;line-height:1;letter-spacing:.3px;text-align:center}
.section-title small{display:block;font-family:"Montserrat",sans-serif;font-weight:400;font-size:6.5px;line-height:1.2;color:var(--muted);letter-spacing:0;margin-top:1px}
.section-title small b{color:var(--ink);font-weight:500}
.divider-band{position:absolute;height:3px;background:var(--line)}
.list{position:absolute;list-style:none;font-size:8px;font-weight:700}
.list li{height:21.4px}
.list--right{text-align:right}
</style>
</head>
<body>
<div class="stage">

  <section class="sheet sheet--front">
    <div class="panel-yellow" style="left:13px;top:82px;width:208px;height:546px"></div>
    <div class="frame" style="left:172px;top:38px;width:210px;height:547px"></div>

    <div class="heading abs" style="left:37px;top:120px">
      <span class="kicker">SIGNATURE</span><span class="main">SANDWICHES</span>
      <span class="note">All served with <b>Rustwood Fries</b></span>
    </div>

    <div class="dish" style="left:37px;top:200px;width:110px"><h4>Turkey Avocado<br>Cream Cheese</h4><p>Smoked turkey, lettuce, tomato, cucumber avocados, cream cheese, &amp; honey mustard on a warm ciabatta bun</p></div>
    <div class="price-tag" style="left:182px;top:200px">9.99</div>
    <div class="dish" style="left:37px;top:281px;width:110px"><h4>French Dip</h4><p>Slow roasted, shaved, beef, provolone cheese, red onion slices, on a 12"hoagie with augus.</p></div>
    <div class="price-tag" style="left:182px;top:281px">9.99</div>
    <div class="dish" style="left:37px;top:341px;width:110px"><h4>Classic Club<br>House Sandwich</h4><p>Ham, Turkey, lettuce, tomato, pickle, onion, bacon, cheddar &amp; swiss cheese, 2 sauce, layered in 3 toasted country style bread slices.</p></div>
    <div class="price-tag" style="left:182px;top:341px">9.99</div>
    <div class="dish" style="left:37px;top:421px;width:100px"><h4>3 Layer Reuben</h4><p>corned beef, kraut, swiss &amp; cheddar cheese, 1000 Island sauce layered in 3 grilled slices of marble rye.</p></div>
    <div class="price-tag" style="left:182px;top:421px">9.99</div>
    <div class="dish" style="left:37px;top:490px;width:110px"><h4>Chicken Club Sandwich</h4><p>Hard breaded chicken beast, proud lone cheese, bacon, lettuce, tomato, pickle all on a brioche bun.</p></div>
    <div class="price-tag" style="left:182px;top:490px">9.99</div>
    <div class="dish" style="left:37px;top:550px;width:110px"><h4>Chicken Quesadilla</h4><p>Fajia seasoned chicken, jack &amp; cheddar cheese, all grilled in a 12" flour tortilla with salad &amp; sauce cream.</p></div>
    <div class="price-tag" style="left:182px;top:550px">9.99</div>

    <div class="heading abs" style="left:255px;top:82px">
      <span class="kicker">COURMET</span><span class="main">BURGERS</span>
      <span class="note">All served with <b>Rustwood Fries</b></span>
    </div>
    <div class="dish" style="left:255px;top:158px;width:95px"><span class="price">9.99</span><h4>Vireau burger</h4><p>Cheddar cheese smoked alam more cheese &amp; bacon.</p></div>
    <div class="dish" style="left:255px;top:227px;width:95px"><span class="price">9.99</span><h4>Swiss Mushroom</h4><p>Swiss cheese, bacon, sauteed mushrooms.</p></div>
    <div class="dish" style="left:255px;top:287px;width:95px"><span class="price">9.99</span><h4>Bacon cheddar</h4><p>Cheddar cheese, bacon on a brioche bun.</p></div>
    <div class="dish" style="left:255px;top:347px;width:95px"><span class="price">9.99</span><h4>Coreat wistern</h4><p>Cheddar cheese, bacon, onion rings &amp; curky's BBQ sauce.</p></div>
    <div class="dish" style="left:255px;top:416px;width:95px"><span class="price">9.99</span><h4>Ranch House Burgers</h4><p>Cheddar cheese, bacon &amp; a fried egg.</p></div>
    <div class="dish" style="left:255px;top:476px;width:95px"><span class="price">9.99</span><h4>Fire House Burger</h4><p>Pepper jack cheese, bacon, grilled onions jalapeños &amp; hot buffalo sauce.</p></div>

    <div class="brand">
      <svg width="18" height="18" viewBox="0 0 18 18" aria-hidden="true"><path d="M2 2 L16 16 M16 2 L2 16" stroke="#222" stroke-width="2"/></svg>
      <div class="intro">This is</div>
      <div class="name">COPPER RANGE</div>
      <div class="served">All served with choice of<b>Potato &amp; Hot Bread</b></div>
    </div>

    <div class="dish" style="left:431px;top:166px;width:100px"><h4>Chicken Fried Steak</h4><p>Hand Breaded of served with Country Coravy.</p></div>
    <div class="price-sm" style="left:542px;top:166px">12.99</div>
    <div class="dish" style="left:431px;top:215px;width:100px"><h4>Parmesian Pepper<br>Press Steak</h4><p>17oz choice tender loin cut, charbroiled of coated with a Parmesian Pepper Crust.</p></div>
    <div class="price-sm" style="left:542px;top:215px">19.99</div>
    <div class="dish" style="left:431px;top:289px;width:100px"><h4>Steak Chateau Briand</h4><p>17oz choice tender loin cut, drizzeled with a Parmesian Cream Sauce of Complimented with grilled Asparagas Spears.</p></div>
    <div class="price-sm" style="left:542px;top:289px">19.99</div>

    <div class="panel-yellow" style="left:591px;top:141px;width:197px;height:244px"></div>
    <div class="dish" style="left:616px;top:166px;width:100px"><h4>Mushroom Coround<br>Sirloin Steak</h4><p>14oz ground sirloin smothered with beef mushroom gravy.</p></div>
    <div class="price-sm" style="left:727px;top:166px">12.99</div>
    <div class="dish" style="left:616px;top:227px;width:100px"><h4>Steak Dei Rio</h4><p>17oz choice tender loin cut rubbed with Bold Southwestern spices, flame broiled, topped with chili pepper butter of fried onion tanglers.</p></div>
    <div class="price-sm" style="left:727px;top:227px">12.99</div>
    <div class="dish" style="left:616px;top:306px;width:100px"><h4>Boston Bleu<br>Cheese Steak</h4><p>12oz choice tender loin cut. Flame broiled topped with meeting Bleu Cheese Crumbles.</p></div>
    <div class="price-sm" style="left:727px;top:306px">12.99</div>

    <div class="frame" style="left:431px;top:436px;width:320px;height:216px"></div>
    <div class="label label--gold label--premium">
      <span class="dot" style="left:14px"></span><span class="dot" style="right:14px"></span>
      <span class="main">VIREAU PREMIUM</span><span class="sub">STEAK SELECTIONS</span>
    </div>
    <div class="center-note" style="left:441px;top:460px;width:300px"><b>- Choice and Prime Corade Beef -</b><br>Served with <b>House Salad</b>, Choice of <b>Potato</b>, and <b>Hot Bread</b></div>

    <div class="dish" style="left:455px;top:498px;width:110px;line-height:1.6"><h4>Filet Mignon</h4><p>Bacon Wrapped.<br>The most tender cut.</p><p><span class="cut">8oz</span><b>24.99</b><br><span class="cut">10oz</span><b>28.99</b></p></div>
    <div class="dish" style="left:455px;top:571px;width:110px;line-height:1.6"><h4>Ribeye Steak</h4><p>Well marbled, rich, full of flavor cut from the prime rib 15oz.</p><b>28.99</b></div>
    <div class="dish" style="left:599px;top:498px;width:130px;line-height:1.6"><h4>Kansas City Strip</h4><p>Firmer texture,<br>Full of Flavor 16oz.</p><b>26.99</b></div>
    <div class="dish" style="left:599px;top:559px;width:130px;line-height:1.6"><h4>Beef Tender Loin Ka-Bob</h4><p>18oz beef tender loin, skewered with bell pepper, onions, tomatos, mushrooms, pineapple, of drizzled with a light Italian marinade.</p><b>26.99</b></div>

    <div class="advisory" style="left:17px;top:647px"><b>Consumer Advisory:</b> Consuming raw or under cooked meat, poultry, seafood, shellfish, or egg may increase your risk of foodborne illness.</div>
  </section>

  <section class="sheet sheet--inside">
    <div class="panel-yellow" style="left:37px;top:37px;width:320px;height:401px"></div>
    <div class="section-title" style="left:37px;top:60px;width:320px">CHICKEN &amp; SEAFOOD<small>Served with choice of <b>Potato &amp; Hot Bread</b></small></div>
    <div class="divider-band" role="img" aria-label="Decorative wavy divider rule" style="left:61px;top:90px;width:272px"></div>

    <div class="dish" style="left:62px;top:117px;width:100px"><span class="price">14.99</span><h4>Charbroiled Chicken<br>Breast</h4><p>10oz Flame broiled breast.</p></div>
    <div class="dish" style="left:62px;top:178px;width:100px"><span class="price">14.99</span><h4>Chicken Fried<br>Chicken Breast</h4><p>10oz hand breaded breast, fried, served with corn on the cob, mashed potatos &amp; country grayvy.</p></div>
    <div class="dish" style="left:62px;top:268px;width:100px"><span class="price">9.99</span><h4>Hand Breaded<br>Chicken Strips</h4><p>Cut &amp; bread per order.</p></div>
    <div class="dish" style="left:62px;top:328px;width:100px"><span class="price">19.99</span><h4>Chicken Ka-Bob</h4><p>10oz charbroiled breast, skewered with bell pepper, onions, mushrooms, tomatoes, pineapple, and drizzeled with light Italian marinade.</p></div>

    <div class="dish" style="left:234px;top:117px;width:115px"><span class="price">19.99</span><h4>North Atlantic Salmon</h4><p>Charbroiled fillet 8oz.</p></div>
    <div class="dish" style="left:234px;top:166px;width:100px"><span class="price">17.99</span><h4>English Style Cod</h4><p>House battered Icelandic cod loin.</p></div>
    <div class="dish" style="left:234px;top:226px;width:118px"><span class="price">17.99</span><h4>Deep Fried Coulf Shrimp</h4><p>6 jumbo shrimp.</p></div>
    <div class="dish" style="left:234px;top:276px;width:100px"><span class="price">19.99</span><h4>Mahi Mahi</h4><p>9oz charbroiled served under a shrimp &amp; mushroom white sauce on a bed of steamed garden vegetables.</p></div>
    <div class="dish" style="left:234px;top:365px;width:110px"><span class="price">12.99</span><h4>Country Fried Catfish</h4><p>Catfish fillets, hand breaded &amp; deep fried.</p></div>

    <svg class="abs" style="left:37px;top:463px" width="136" height="12" viewBox="0 0 136 12" aria-hidden="true"><path d="M0 1 H136 M1 1 V10 M1 1 L7 7 M135 1 V10 M135 1 L129 7" stroke="#222" stroke-width="2" fill="none"/></svg>
    <div class="section-title" style="left:37px;top:474px;width:136px;font-weight:400">SIDES</div>
    <ul class="list" style="left:37px;top:507px">
      <li>Steamed Coarden Vegetables</li><li>Twice Baked Potato</li><li>Loaded Baked &amp; Mashed Potato</li><li>Corilled Asparagus</li><li>House or Coasar Salad</li><li>*If in place of potato, add 2.99</li>
    </ul>

    <div class="frame" style="left:221px;top:480px;width:136px;height:157px"></div>
    <div class="label label--gold" style="left:262px;top:464px;width:95px;height:33px;font-size:18px;line-height:33px">BAKED</div>
    <ul class="list list--right" style="left:221px;top:507px;width:115px">
      <li>Baked</li><li>Mashed</li><li>American Fries</li><li>Coerman Fries</li><li>French Fries</li><li>Onion Rings</li>
    </ul>

    <div class="advisory" style="left:37px;top:648px"><b>Consumer Advisory:</b> Consuming raw or under cooked meat, poultry, seafood, shellfish, or egg may increase your risk of foodborne illness.</div>

    <div class="frame" style="left:430px;top:54px;width:370px;height:315px"></div>
    <div class="label label--gold" style="left:579px;top:37px;width:209px;height:33px;font-size:18px;line-height:33px">APPETIZERS</div>
    <div class="dish" style="left:463px;top:88px;width:115px"><span class="price">8.99</span><h4>Fries Mozzarella<br>Cheese Sticks</h4><p>Hand breaded sticks serverd with marinara sauce.</p></div>
    <div class="dish" style="left:463px;top:159px;width:100px"><span class="price">8.99</span><h4>French Fried Pickles</h4><p>Basket full of House breaded pickles with Ranch Dressing.</p></div>
    <div class="dish" style="left:463px;top:229px;width:100px"><span class="price">8.99</span><h4>Onion Ring Tower</h4></div>
    <div class="dish" style="left:463px;top:268px;width:100px"><span class="price">9.99</span><h4>Cheddar Cheese<br>Ialapend Poppers</h4><p>Fried Cheddar cheese stuffed jalpenos with Ranch Dressing (10).</p></div>
    <div class="dish" style="left:644px;top:88px;width:110px"><span class="price">12.99</span><h4>Calamari</h4><p>Hand breaded &amp; served with cocktail sauce</p></div>
    <div class="dish" style="left:644px;top:146px;width:110px"><span class="price">11.99</span><h4>Shrimp Cocktail</h4><p>10 chilled shrimp with cocktail sauce .</p></div>
    <div class="dish" style="left:644px;top:204px;width:120px"><span class="price">9.99</span><h4>Macho Nachos</h4><p>Corn tortilla chips, refried beans, taco meat, chili, cheese, salad, lettuce, tomato, jalapeños, &amp; sour cream.</p></div>
    <div class="dish" style="left:644px;top:283px;width:120px"><span class="price">12.99</span><h4>Rocky Mountain Oysters</h4><p>Full pund of breaded &amp; fried oysters served with Horseradish sauce.</p></div>

    <div class="frame" style="left:430px;top:383px;width:370px;height:320px"></div>
    <div class="label label--gold" style="left:579px;top:360px;width:209px;height:33px;font-size:18px;line-height:33px">SALADS</div>
    <div class="dish" style="left:463px;top:410px;width:110px"><span class="price">9.99</span><h4>Classic Chef Salad</h4><p>Tossed Iceburg, cheese, tomato, cucumber, egg, ham, turkey, bacon, croutons, and a garlic breadstick.</p></div>
    <div class="dish" style="left:463px;top:498px;width:115px"><span class="price">9.99</span><h4>Blackened Chicken<br>Southwest Salad</h4><p>Blackened chicken served over iceburg lettuce, cheese, tomato, sweet corn, black beans, black olives, avonados, sour cream, tortilla chips, &amp; southwest dressing.</p></div>
    <div class="dish" style="left:644px;top:410px;width:118px"><span class="price">9.99</span><h4>West Coast Berry Salad</h4><p>Romaine lettuce, blue cheese, egg, tomato, black &amp; blue berries, strawbarries, pineapple, oranges, almonds, pandied walnuts, cranberries, chicken or shrimp.</p></div>
    <div class="dish" style="left:644px;top:510px;width:115px"><span class="price">9.99</span><h4>Chicken Salad</h4><p>Fried or charbroiled chicken oven iceburg, lethiss, cheese, egg, tomato, cucumbers, bacon croutons &amp; a gaplic breadstick.</p></div>
    <div class="dish" style="left:547px;top:610px;width:120px;text-align:center"><span class="price">9.99</span><h4>Caprese Salad</h4><p>Fresh baby spinach, balsamic vinegar, basil.</p></div>
  </section>

</div>
</body>
</html>
```